Flyer for the Harvest of lanterns conference

Flyer design for an annual international conference called "VELMARK 2017". This is a conference for young adults, so we hope to produce a design that is both professional and appealing to young people in general

We'd like the flyer to showcase the conference brand logo, and clearly highlight the key information to people who will read it.

Target Market(s)

Young people, young adults

Industry/Entity Type

Religious

Font styles to use
Sans Serif

Colors

Designer to choose colors to be used in the design.

Requirements
Must have
• - Should be only one page (Vertical or Horizontal).
• - the VELMAK logo and all the information found in the attached text file. This includes: Main topic: Your sons and daughters shall prophesy,
• Dates and time, location, contact information and everything that is in the attached text file.
Nice to have
• It would be nice to see samples where the white logo is used and another where the black one is used.
Should not have
• This is NOT a folded flyer, we will be sticking it on doors and public places. And we will be printing large simple to put on walls. So only one page with few words like an add (the words are in the attached file)

```html
<!DOCTYPE html>
<html lang="en">
<head>
<meta charset="utf-8">
<title>VELMARK 2017 – Harvest of Lanterns Conference</title>
<link rel="stylesheet" href="https://fonts.googleapis.com/css2?family=Lato:wght@400;700;900&display=swap">
<style>
  :root {
    --stage: #5f5f61;
    --night: #0d0c10;
    --orange: #f7941d;
    --gold: #f9b53a;
    --ink: #2b2b2b;
    --panel: #e6e7e8;
    --paper: #ffffff;
  }
  * { margin: 0; padding: 0; box-sizing: border-box; }
  html, body { width: 800px; height: 1200px; overflow: hidden; }
  body {
    background: var(--stage);
    font-family: 'Lato', sans-serif;
    position: relative;
  }
  .flyer {
    position: absolute;
    left: 20px; top: 62px;
    width: 760px; height: 1075px;
    background: var(--paper);
    overflow: hidden;
  }
  .hero {
    position: absolute; left: 0; top: 0;
    width: 760px; height: 465px;
    background:
      radial-gradient(ellipse 260px 200px at 540px 230px, rgba(255,170,60,0.55), rgba(150,60,20,0.25) 55%, transparent 80%),
      radial-gradient(ellipse 520px 120px at 380px 420px, rgba(200,90,30,0.6), transparent 75%),
      linear-gradient(180deg, #09080b 0%, #141018 45%, #2a1612 80%, #3b1a10 100%);
  }
  .brand {
    position: absolute; left: 46px; top: 34px;
    width: 200px; text-align: center;
  }
  .brand-dot {
    width: 92px; height: 92px; border-radius: 50%;
    background: var(--orange);
    margin: 0 auto 18px;
  }
  .brand-name {
    color: #ffffff; font-weight: 700; font-size: 28px; letter-spacing: 3px;
  }
  .event-title {
    position: absolute; left: 0; top: 345px; width: 760px;
    text-align: center; color: var(--gold);
    font-weight: 900; font-size: 56px; line-height: 1;
  }
  .event-subtitle {
    position: absolute; left: 0; top: 410px; width: 760px;
    text-align: center; color: #ffffff;
    font-weight: 400; font-size: 32px; line-height: 1; letter-spacing: 0.5px;
  }
  .theme-band {
    position: absolute; left: 0; top: 465px;
    width: 760px; height: 120px;
    background: var(--orange);
    display: flex; align-items: center; justify-content: center;
  }
  .theme {
    color: #ffffff; font-weight: 900; font-size: 43px; line-height: 1.1;
    text-align: center; text-transform: uppercase;
    text-shadow: 2px 2px 3px rgba(0,0,0,0.45);
  }
  .details-area {
    position: absolute; left: 0; top: 585px;
    width: 760px; height: 431px;
    background: linear-gradient(90deg, #ffffff 0%, #f4f4f4 100%);
  }
  .speakers {
    position: absolute; left: 48px; top: 100px;
  }
  .speakers h2 {
    color: var(--orange); font-weight: 700; font-size: 29px; margin-bottom: 14px;
  }
  .speaker-list { list-style: none; }
  .speaker-list li {
    display: flex; align-items: center; gap: 12px;
    height: 49px;
    color: var(--ink); font-weight: 700; font-size: 19px;
  }
  .tick { width: 18px; height: 18px; flex: none; }
  .info-panel {
    position: absolute; left: 403px; top: 46px;
    width: 357px; height: 347px;
    background: var(--panel);
    border-radius: 30px 0 0 30px;
    padding: 38px 0 0 40px;
  }
  .info-item { margin-bottom: 16px; }
  .info-label {
    color: var(--orange); font-size: 16px; font-weight: 400; line-height: 1.3;
  }
  .info-value {
    color: var(--ink); font-size: 16.5px; font-weight: 700; line-height: 1.3;
  }
  .contact-band {
    position: absolute; left: 0; top: 1016px;
    width: 760px; height: 59px;
    background: var(--orange);
    display: flex; align-items: center; justify-content: center;
    color: #ffffff; font-weight: 700; font-size: 16px;
  }
</style>
</head>
<body>
  <main class="flyer">
    <section class="hero" role="img" aria-label="Photo: silhouette of a kneeling person before a cross against a glowing sunset sky"></section>

    <div class="brand">
      <div class="brand-dot"></div>
      <div class="brand-name">VELMAK</div>
    </div>

    <h1 class="event-title">VELMARK 2017</h1>
    <p class="event-subtitle">HARVEST OF LANTERNS CONFERENCE</p>

    <section class="theme-band">
      <p class="theme">Your sons and daughters<br>shall prophesy</p>
    </section>

    <section class="details-area">
      <div class="speakers">
        <h2>Speakers:</h2>
        <ul class="speaker-list">
          <li><svg class="tick" viewBox="0 0 20 20"><circle cx="10" cy="10" r="8" fill="none" stroke="#f7941d" stroke-width="1.6"/><path d="M6 10.5l3 3 6-7" fill="none" stroke="#f7941d" stroke-width="1.8"/></svg>Pastor Remi Olandu</li>
          <li><svg class="tick" viewBox="0 0 20 20"><circle cx="10" cy="10" r="8" fill="none" stroke="#f7941d" stroke-width="1.6"/><path d="M6 10.5l3 3 6-7" fill="none" stroke="#f7941d" stroke-width="1.8"/></svg>Bishop Aaron Melisk</li>
          <li><svg class="tick" viewBox="0 0 20 20"><circle cx="10" cy="10" r="8" fill="none" stroke="#f7941d" stroke-width="1.6"/><path d="M6 10.5l3 3 6-7" fill="none" stroke="#f7941d" stroke-width="1.8"/></svg>Prophet Jonas Teravi Lumbo</li>
          <li><svg class="tick" viewBox="0 0 20 20"><circle cx="10" cy="10" r="8" fill="none" stroke="#f7941d" stroke-width="1.6"/><path d="M6 10.5l3 3 6-7" fill="none" stroke="#f7941d" stroke-width="1.8"/></svg>Prophet Noel Baraka</li>
          <li><svg class="tick" viewBox="0 0 20 20"><circle cx="10" cy="10" r="8" fill="none" stroke="#f7941d" stroke-width="1.6"/><path d="M6 10.5l3 3 6-7" fill="none" stroke="#f7941d" stroke-width="1.8"/></svg>Prophet Samuel Ditenda</li>
        </ul>
      </div>

      <aside class="info-panel">
        <div class="info-item">
          <div class="info-label">Date:</div>
          <div class="info-value">September 1st, 2nd and 3rd 2017</div>
        </div>
        <div class="info-item">
          <div class="info-label">Start Time:</div>
          <div class="info-value">6:00PM</div>
        </div>
        <div class="info-item">
          <div class="info-label">Location:</div>
          <div class="info-value">Harborview Lantern Inn<br>412 Cedar Avenue<br>Westbrook Falls, ME 04999 United</div>
        </div>
        <div class="info-item">
          <div class="info-label">Rooms:</div>
          <div class="info-value">Maplecrest Ballroom</div>
        </div>
      </aside>
    </section>

    <footer class="contact-band">
      Tel:+1 (555) 014 2290 | Email:hello@lanterngrove.org | Website: http://velmak.org
    </footer>
  </main>
</body>
</html>
```